Looking for business card/letterhead/email signature

Take existing logo and create full design suite of collateral

Contact Information for Business Card

Use mock details that can be edited by us

Font styles to use
Sans Serif

```html
<!DOCTYPE html>
<html lang="en">
<head>
<meta charset="utf-8">
<title>Marlow Digital – Stationery Suite</title>
<link href="https://fonts.googleapis.com/css2?family=Roboto:wght@400;700&display=swap" rel="stylesheet">
<style>
  :root{
    --bg:#e4e4e4;
    --paper:#ffffff;
    --paper-soft:#f4f4f4;
    --brand:#0b4f93;
    --brand-line:#3a6fab;
    --ink:#4a4f57;
    --s1:#0b4f93;
    --s2:#3d9ad6;
    --s3:#d8cf3a;
    --s4:#f08a2c;
    --s5:#e2457a;
    --s6:#d9263b;
  }
  *{box-sizing:border-box;margin:0;padding:0}
  html,body{width:1200px;height:796px;overflow:hidden}
  body{background:var(--bg);font-family:"Roboto",Arial,sans-serif;position:relative;color:var(--ink)}
  .piece{position:absolute;box-shadow:0 2px 6px rgba(0,0,0,.12);overflow:hidden}

  /* company name */
  .brand-name{position:absolute;color:var(--brand);font-weight:400;line-height:1;white-space:nowrap;letter-spacing:.01em}
  .brand-name.centered{left:50%;transform:translateX(-50%)}
  .brand-name.on-brand{color:#fff}

  /* colour stripe */
  .stripe{position:absolute;left:0;right:0;display:flex;gap:2px;height:2px}
  .stripe span{flex:1}
  .stripe span:nth-child(1){background:var(--s1)}
  .stripe span:nth-child(2){background:var(--s2)}
  .stripe span:nth-child(3){background:var(--s3)}
  .stripe span:nth-child(4){background:var(--s4)}
  .stripe span:nth-child(5){background:var(--s5)}
  .stripe span:nth-child(6){background:var(--s6)}
  .band{position:absolute;left:0;right:0;bottom:0;background:var(--brand);color:#fff;text-align:center}

  /* letterhead */
  .letterhead{left:342px;top:78px;width:336px;height:472px;background:var(--paper)}
  .letterhead .brand-name{font-size:17px;top:58px}
  .letter{position:absolute;left:30px;top:136px;width:267px;font-size:4.3px;line-height:1.65;color:#6b6f75}
  .letter .salute{font-size:7.2px;color:#555;margin-bottom:12px}
  .letter p{margin-bottom:6px;text-align:justify}
  .signature{width:62px;height:22px;margin-top:4px;background:linear-gradient(90deg,#dfe8f4,#c9d8ec);border-radius:3px}
  .letterhead .stripe{top:446px}
  .letterhead .band{height:22px;font-size:4.4px;line-height:7px;padding-top:4px}

  /* folder */
  .folder{left:706px;top:50px;width:242px;height:500px;background:var(--brand)}
  .folder .spine{position:absolute;top:0;bottom:0;width:1px;background:var(--brand-line)}
  .folder .brand-name{font-size:26px;top:252px;left:128px}

  /* business cards */
  .card-front{left:158px;top:358px;width:152px;height:86px;background:var(--brand)}
  .card-front .brand-name{font-size:13px;top:34px}
  .card-front .web{position:absolute;left:0;right:0;top:73px;text-align:center;font-size:3.6px;letter-spacing:.12em;color:#fff}

  .card-back{left:158px;top:462px;width:154px;height:87px;background:var(--paper-soft)}
  .card-back .who{position:absolute;left:12px;top:26px;color:var(--brand);font-size:6px;font-weight:700;line-height:1}
  .card-back .who small{display:block;font-size:3.6px;font-weight:400;margin-top:1px}
  .card-back .brand-name{font-size:9px;right:11px;top:27px}
  .card-back .stripe{top:56px;height:1.5px}
  .card-back .band{height:28px;font-size:3.6px;line-height:5.2px;padding-top:5px}

  .card-large{left:42px;top:606px;width:305px;height:148px;background:var(--paper-soft)}
  .card-large .who{position:absolute;left:23px;top:44px;color:var(--brand);font-size:11.5px;font-weight:700;line-height:1}
  .card-large .who small{display:block;font-size:7px;font-weight:400;margin-top:2px}
  .card-large .brand-name{font-size:16px;right:26px;top:48px}
  .card-large .stripe{top:95px;height:2px}
  .card-large .band{height:50px;font-size:7px;line-height:10px;padding-top:6px}

  /* envelopes */
  .envelope-front{left:369px;top:580px;width:386px;height:176px;background:var(--paper-soft)}
  .envelope-front .brand-name{font-size:18px;left:22px;top:44px}
  .envelope-front .return{position:absolute;left:22px;top:74px;font-size:4.2px;line-height:5.6px;color:#555}
  .envelope-front .stripe{top:161px}
  .envelope-front .band{height:12px}

  .envelope-back{left:774px;top:578px;width:386px;height:176px;background:var(--paper-soft)}
  .envelope-back .flap{position:absolute;left:0;right:0;top:0;height:55px;background:var(--brand);border-radius:0 0 34px 34px}
  .envelope-back .brand-name{font-size:11px;top:26px}
</style>
</head>
<body>

<section class="piece letterhead">
  <div class="brand-name centered">Marlow Digital</div>
  <div class="letter">
    <div class="salute">Dear Mr. Carter,</div>
    <p>Thank you for meeting with our team last week. We enjoyed learning about your goals for the coming year and have prepared a plan that covers design, content and launch support for your new website.</p>
    <p>The first phase focuses on research and structure. We will review your current pages, interview key staff and map the journeys your customers take before sketching any screens.</p>
    <p>In the second phase we build the visual system, test it with real users and refine every detail. Weekly check-ins keep you informed and give room for feedback at each step.</p>
    <p>Please review the attached proposal and let us know a good time to talk through the next steps.</p>
    <p>Sincerely,</p>
    <div class="signature" role="img" aria-label="Handwritten signature of Avery Lane"></div>
  </div>
  <div class="stripe"><span></span><span></span><span></span><span></span><span></span><span></span></div>
  <div class="band">1420 Cedar Row, Juneau, Alaska 99801<br>555 210 4417 · 555 384 9021 · 555 672 1308 · hello@marlowdigital.com · www.marlowdigital.com</div>
</section>

<section class="piece folder">
  <span class="spine" style="left:11px"></span>
  <span class="spine" style="left:18px"></span>
  <span class="spine" style="left:23px"></span>
  <div class="brand-name centered on-brand">Marlow Digital</div>
</section>

<section class="piece card-front">
  <div class="brand-name centered on-brand">Marlow Digital</div>
  <div class="web">www.marlowdigital.com</div>
</section>

<section class="piece card-back">
  <div class="who">AVERY LANE<small>CEO/FOUNDER</small></div>
  <div class="brand-name">Marlow Digital</div>
  <div class="stripe"><span></span><span></span><span></span><span></span><span></span><span></span></div>
  <div class="band">1420 Cedar Row, Juneau, Alaska 99801<br>555 210 4417 · 555 384 9021 · 555 672 1308 · hello@marlowdigital.com<br>www.marlowdigital.com</div>
</section>

<section class="piece card-large">
  <div class="who">AVERY LANE<small>CEO/FOUNDER</small></div>
  <div class="brand-name">Marlow Digital</div>
  <div class="stripe"><span></span><span></span><span></span><span></span><span></span><span></span></div>
  <div class="band">1420 Cedar Row, Juneau, Alaska 99801<br>555 210 4417 · 555 384 9021 · 555 672 1308 · hello@marlowdigital.com<br>www.marlowdigital.com</div>
</section>

<section class="piece envelope-front">
  <div class="brand-name">Marlow Digital</div>
  <div class="return">1420 Cedar Row<br>Juneau, Alaska 99801</div>
  <div class="stripe"><span></span><span></span><span></span><span></span><span></span><span></span></div>
  <div class="band"></div>
</section>

<section class="piece envelope-back">
  <div class="flap">
    <div class="brand-name centered on-brand">Marlow Digital</div>
  </div>
</section>

</body>
</html>
```